依頼詳細
診療時間変更に際し、案内チラシを配ろうと思います。そのチラシデザイン制作をお願い致します。特に、3つの特徴をアピールしたいです。1)日曜日も受付していること2)大型駐車場で楽々駐車できること3)待ち時間が少ない。写真を効果的に使い、安心感と通ってみたくなる雰囲気にしてもらいたいです。
記載項目
日曜も受付!!/ルナヒル整骨院/048-312-7759/http://hana-riku.com/確かな技術・優しい治療・丁寧な症状説明/ロゴ(添付ファイル)/料金目安/施術項目/施術の流れ/あいさつ/受付時間/写真その他、詳細文章は添付ファイルのチラシ参照
サイズ
A4
ページ数
片面
希望イメージ
シンプル 複雑
単色 カラフル
暗い 明るい
日常 高級
遊び心 厳粛
未来的 伝統的
女性的 男性的
希望する色
アイボリー、オレンジ
納品ファイル
• 高解像度JPG (.jpg)
• イラストレーター形式 (.ai)
補足説明
院内・院外・施術画像多数あります。連絡いただけましたら、メールにてお送りいたします。
どうぞ、よろしくお願いいたします。
チラシのサンプルデータをアップします。
9月よりスタッフを増員して、年中無休の診療体制となります。
その案内のために、今回のチラシが必要となりました。

1)日曜日・祝日は、午前診療のみで9:30~13:00です。※祝日は不定休です。
2)レイアウトは横でお願いします。
3)待ち時間が少ないとは、具体的に、施術者が多いので比較的待ち時間が少ないです。
4)チラシは、ポスティングと新聞折り込みで配布予定です。
チラシ用の画像をオンラインストレージにアップしておきました。
作成の際、ご利用いただけましたら幸いです。

http://kumobako.jp/download/a3b7c1e9f0d24b6a8c5e7f1d2b9a0c4e6f8d1a2b
オンラインストレージのデータが期限切れとなり、
削除されておりましたので、再度アップいたしました。

http://kumobako.jp/download/b4c8d2f0a1e35c7b9d6f8a2e3c0b1d5f7a9e2b3c

mikuさんの提案は、センスがよく、即気に入りました。ぱっと見わかりやすく、印象が良く、とてもよかったです。当院のロゴをアレンジしてUSPを入れる心憎い演出も気に入りました。修正のレスポンスも早く、スムーズにイメージ以上のデザインし仕上げて頂きました。ありがとうございました。

この度は、当院のチラシデザインのご提案をいただきまして、誠にありがとうございました。お陰さまで、とても気に入った作品に巡り合えました。感謝申し上げます。
ルナヒル整骨院 森下健二

```html
<!DOCTYPE html>
<html lang="ja">
<head>
<meta charset="utf-8">
<title>ルナヒル整骨院 案内チラシ</title>
<link href="https://fonts.googleapis.com/css2?family=M+PLUS+Rounded+1c:wght@500;800&family=Noto+Sans+JP:wght@400;700&display=swap" rel="stylesheet">
<style>
:root{
  --orange:#e8821e;
  --orange-deep:#d9691a;
  --orange-soft:#f6c27f;
  --ivory:#f5ecdc;
  --ivory-deep:#ead9bd;
  --brown:#5b4129;
  --brown-dark:#3e2b1a;
  --text:#3a2a1c;
  --white:#ffffff;
}
*{margin:0;padding:0;box-sizing:border-box}
html,body{width:1200px;height:848px;overflow:hidden}
body{font-family:"Noto Sans JP",sans-serif;color:var(--text);background:var(--ivory)}
.flyer{position:relative;width:1200px;height:848px;overflow:hidden;background:linear-gradient(180deg,var(--ivory) 0%,var(--ivory-deep) 100%)}
.abs{position:absolute}
.nowrap{white-space:nowrap}
.photo{position:absolute}
.photo-team{left:0;top:0;width:600px;height:396px;background:linear-gradient(160deg,#efe6dc 0%,#d9c7b4 55%,#b89d86 100%)}
.photo-treatment{left:600px;top:0;width:600px;height:330px;background:linear-gradient(120deg,#cfc3b3 0%,#e9e1d6 45%,#8b6a4e 100%)}

/* feature badges */
.badge{position:absolute;border-radius:50%;background:var(--white);border:3px solid var(--orange);text-align:center;display:flex;flex-direction:column;align-items:center;justify-content:center;box-shadow:0 2px 4px rgba(0,0,0,.2)}
.badge-sunday{left:58px;top:228px;width:140px;height:140px}
.badge-wait{left:202px;top:232px;width:134px;height:134px}
.badge-parking{left:370px;top:218px;width:152px;height:152px;justify-content:flex-start;padding-top:18px}
.badge .lead{font-family:"M PLUS Rounded 1c",sans-serif;font-weight:800;color:var(--orange-deep);font-size:18px;line-height:1.15;white-space:nowrap}
.badge .time{font-weight:700;color:var(--brown);font-size:14px;margin-top:4px}
.badge .note{font-size:10px;color:var(--brown);margin-top:3px;line-height:1.3;white-space:nowrap}
.parking-photo{width:96px;height:50px;margin-top:6px;background:linear-gradient(180deg,#b9c6cf 0%,#8f9aa3 60%,#6d7880 100%)}
.badge-count{position:absolute;left:508px;top:230px;width:62px;height:62px;border-radius:50%;background:var(--orange);color:var(--white);font-family:"M PLUS Rounded 1c",sans-serif;font-weight:800;font-size:13px;display:flex;align-items:center;justify-content:center;border:2px solid var(--white)}

/* greeting */
.greeting{left:960px;top:30px;width:232px;background:var(--white);border-radius:6px;padding:12px;box-shadow:0 1px 4px rgba(0,0,0,.15)}
.greeting-title{font-family:"M PLUS Rounded 1c",sans-serif;font-weight:800;color:var(--orange-deep);font-size:17px}
.greeting-portrait{position:absolute;right:10px;top:8px;width:66px;height:66px;background:linear-gradient(180deg,#e2c6a8,#b58f70)}
.greeting p{font-size:11.5px;line-height:1.6;margin-top:8px;width:136px}
.greeting p.wide{width:auto;margin-top:0}
.greeting .sign{text-align:right;font-size:10px;margin-top:6px}
.greeting .sign b{display:block;font-size:15px}

/* ribbon */
.ribbon{left:0;top:0;width:1200px;height:848px;pointer-events:none}
.ribbon-text{left:24px;top:386px;transform:rotate(-3deg);transform-origin:left top;color:var(--white);white-space:nowrap}
.ribbon-text .line1{font-family:"M PLUS Rounded 1c",sans-serif;font-weight:800;font-size:28px;letter-spacing:1px;line-height:1.3}
.ribbon-text .line1 small{font-size:21px;margin-left:12px}
.ribbon-text .line2{font-family:"M PLUS Rounded 1c",sans-serif;font-weight:800;font-size:28px;line-height:1.3;margin-top:4px;display:flex;align-items:center;gap:8px}
.dot-mark{width:22px;height:22px;border-radius:50%;background:var(--white);display:inline-block;flex:none}

/* facility */
.wide-label{left:622px;top:348px;background:var(--orange);color:var(--white);font-family:"M PLUS Rounded 1c",sans-serif;font-weight:800;font-size:16px;padding:4px 10px;transform:rotate(-5deg);border:2px solid var(--white);white-space:nowrap;z-index:2}
.room{position:absolute;border:4px solid var(--white);box-shadow:0 2px 4px rgba(0,0,0,.2)}
.room span{position:absolute;right:4px;bottom:2px;font-size:11px;background:rgba(255,255,255,.85);padding:0 4px}
.room-wait{left:630px;top:392px;width:138px;height:90px;background:linear-gradient(180deg,#f3efe6,#9fc15a 70%,#8a6b4a)}
.room-kids{left:774px;top:376px;width:162px;height:98px;background:linear-gradient(180deg,#f1ede6,#c9b79f 60%,#9a7a5a)}
.room-treat{left:942px;top:338px;width:144px;height:130px;background:linear-gradient(180deg,#e4d8c6,#8d6a4a)}
.room-wc{left:1090px;top:338px;width:110px;height:96px;background:linear-gradient(180deg,#6a5140,#c9a981)}
.kids-tag{left:786px;top:340px;width:54px;height:54px;border-radius:50%;background:var(--orange);color:var(--white);font-size:10px;font-weight:700;display:flex;align-items:center;justify-content:center;text-align:center;line-height:1.2;z-index:2}

/* sections */
.circle-tag{position:absolute;border-radius:50%;background:var(--orange);color:var(--white);font-family:"M PLUS Rounded 1c",sans-serif;font-weight:800;font-size:15px;display:flex;align-items:center;justify-content:center;text-align:center;line-height:1.2}
.tag-promise{left:30px;top:496px;width:86px;height:86px;transform:rotate(-8deg)}
.tag-care{left:624px;top:500px;width:72px;height:72px}
.section-title{position:absolute;font-family:"M PLUS Rounded 1c",sans-serif;font-weight:800;color:var(--brown-dark);white-space:nowrap}
.title-promise{left:138px;top:498px;font-size:21px}
.title-care{left:706px;top:502px;font-size:20px}

.promise{position:absolute;top:540px}
.promise .num{font-weight:700;font-size:12px;line-height:14px;color:var(--brown)}
.promise h3{font-family:"M PLUS Rounded 1c",sans-serif;font-weight:800;color:var(--orange-deep);font-size:20px;line-height:24px;white-space:nowrap}
.promise p{font-size:11.5px;line-height:1.5;margin-top:2px}
.promise .small{font-size:9.5px;color:var(--brown);margin-top:2px;line-height:1.3}
.p1{left:128px;width:124px}.p2{left:262px;width:152px}.p3{left:424px;width:188px}
.promise-photo{position:absolute}
.pp1{left:30px;top:656px;width:70px;height:74px;background:linear-gradient(180deg,#f4efe5,#d6c7ad)}
.pp1b{left:108px;top:662px;width:144px;height:68px;background:linear-gradient(180deg,#efe4d4,#d3b896)}
.pp2{left:262px;top:656px;width:152px;height:74px;background:linear-gradient(180deg,#efe7dc,#a9805b)}
.pp3{left:424px;top:656px;width:188px;height:74px;background:linear-gradient(180deg,#efe7dc,#6a5140)}

/* pain list */
.bubble{left:968px;top:488px;background:var(--white);border:2px solid var(--orange);border-radius:18px;color:var(--orange-deep);font-family:"M PLUS Rounded 1c",sans-serif;font-weight:800;font-size:14px;padding:3px 12px;transform:rotate(-3deg);white-space:nowrap}
.pains{left:706px;top:536px;width:480px;font-size:12.5px;font-weight:700;line-height:18px}
.pain-row{display:flex}
.pain-row span{display:flex;align-items:center;gap:4px;white-space:nowrap}
.pain-row span::before{content:"";width:9px;height:9px;background:var(--orange);display:inline-block;flex:none}
.pain-row span.hi{color:var(--orange-deep)}
.w1{width:146px}.w2{width:70px}.w3{width:82px}.w4{width:82px}

/* steps */
.steps{left:624px;top:604px;width:288px;height:118px;background:var(--white);border:2px solid var(--orange-soft);border-radius:4px;overflow:hidden}
.steps-head{display:flex;align-items:center;gap:8px;background:var(--orange);color:var(--white);font-weight:700;font-size:13px;padding:2px 8px;white-space:nowrap}
.steps-head small{font-size:9.5px;font-weight:400}
.step-row{display:flex;gap:4px;padding:4px}
.step{flex:1;text-align:center;min-width:0}
.step i{display:inline-block;width:16px;height:16px;border-radius:50%;background:var(--orange);color:var(--white);font-style:normal;font-size:10px;line-height:16px}
.step b{display:block;background:var(--orange-soft);color:var(--brown-dark);font-size:11px;line-height:16px;margin-top:1px;white-space:nowrap}
.step em{display:block;font-style:normal;font-size:8px;line-height:1.2;margin-top:2px;height:20px;white-space:nowrap}
.step .shot{height:28px;margin-top:2px;background:linear-gradient(180deg,#e6dccd,#9f8066)}

.insurance{left:1060px;top:592px;background:var(--orange);color:var(--white);font-family:"M PLUS Rounded 1c",sans-serif;font-weight:800;font-size:15px;padding:4px 10px;text-align:center;line-height:1.2;white-space:nowrap}
.insurance small{display:block;font-size:10px;font-family:"Noto Sans JP",sans-serif;font-weight:400}
.price{left:922px;top:624px;width:150px}
.price h4{font-size:15px;font-weight:700;color:var(--brown-dark);line-height:20px}
.price table{border-collapse:collapse;font-size:12px;margin-top:2px;white-space:nowrap}
.price td{padding:1px 3px;line-height:16px}
.price .ins{background:var(--orange);color:var(--white);font-size:9px;border-radius:3px;line-height:1.1;text-align:center}
.price-note{left:922px;top:702px;font-size:9px;white-space:nowrap}

/* footer */
.footer{left:0;top:738px;width:1200px;height:110px;background:var(--brown)}
.foot-brand{left:30px;top:752px;color:var(--white)}
.foot-brand .name{display:flex;align-items:center;gap:8px;font-family:"M PLUS Rounded 1c",sans-serif;font-weight:800;font-size:27px;white-space:nowrap}
.foot-brand .sub{font-family:"M PLUS Rounded 1c",sans-serif;font-weight:800;font-size:17px;margin-top:10px;color:var(--orange-soft);white-space:nowrap}
.foot-brand .sub span{font-size:12px;color:var(--white);margin-left:8px}
.schedule{left:300px;top:752px;border-collapse:collapse;background:var(--white);font-size:11px;text-align:center}
.schedule th,.schedule td{border:1px solid var(--brown);padding:1px 5px;height:22px}
.schedule th{background:var(--orange-soft);font-weight:700;white-space:nowrap}
.schedule th.time{width:88px}
.schedule td.time{font-size:10px;line-height:1.15;text-align:left;white-space:nowrap}
.schedule .dot{color:var(--brown-dark);font-size:12px}
.contact{left:626px;top:744px;color:var(--white);width:324px}
.contact .where{font-size:10.5px;color:var(--orange-soft);text-align:right;line-height:14px}
.contact .addr{font-size:11.5px;line-height:15px;white-space:nowrap}
.contact .tel{display:flex;align-items:center;gap:8px;font-weight:700;font-size:24px;line-height:30px;margin-top:1px;white-space:nowrap}
.contact .tel span{font-size:12px;line-height:18px;background:var(--orange);padding:1px 8px;font-weight:700}
.contact .url{display:flex;align-items:center;gap:6px;font-size:13px;margin-top:2px;white-space:nowrap}
.contact .search{background:var(--white);color:var(--text);font-size:10px;padding:1px 6px}
.contact .search-btn{background:var(--ivory-deep);color:var(--text);font-size:10px;padding:1px 6px}
.map{left:962px;top:718px;width:232px;height:124px;background:linear-gradient(135deg,#fbf8f2,#e9e2d4);border:2px solid var(--white)}
</style>
</head>
<body>
<div class="flyer">

  <div class="photo photo-team" role="img" aria-label="白衣姿のスタッフ集合写真"></div>
  <div class="photo photo-treatment" role="img" aria-label="院長が施術台で患者に施術している様子"></div>

  <svg class="abs ribbon" viewBox="0 0 1200 848" aria-hidden="true">
    <polygon points="0,372 612,336 604,440 0,488" fill="#e8821e"/>
    <polygon points="0,488 604,440 604,446 0,494" fill="#f6c27f" opacity=".7"/>
  </svg>

  <div class="badge badge-sunday">
    <div class="lead">日曜日・<br>祝日も受付!!</div>
    <div class="time">9:30~13:00</div>
    <div class="note">※祝日は不定休です。</div>
  </div>
  <div class="badge badge-wait">
    <div class="lead">お待たせ<br>しません!!</div>
    <div class="note">スタッフを増員して<br>パワーアップ!</div>
  </div>
  <div class="badge badge-parking">
    <div class="lead">大型駐車場<br>完備!!</div>
    <div class="parking-photo" role="img" aria-label="院の外観と広い駐車場"></div>
  </div>
  <div class="badge-count">500台分!</div>

  <section class="abs greeting">
    <div class="greeting-title">ごあいさつ</div>
    <div class="greeting-portrait" role="img" aria-label="院長の顔写真"></div>
    <p>皆さまの健康作りに貢献できますよう、スタッフ一丸となり、精進して参ります。</p>
    <p class="wide">何かお困りの際は、お気軽にいらしてください。確かな技術・優しい治療・丁寧な症状説明をモットーに、しっかりと施術させていただきます。</p>
    <div class="sign">ルナヒル整骨院 院長<b>森下 健二</b></div>
  </section>

  <div class="abs ribbon-text">
    <div class="line1">若宮でクチコミNo.1<small>地域を愛する整骨院</small></div>
    <div class="line2"><span class="dot-mark"></span><span>ルナヒル整骨院</span><span>が更に便利で身近に!!</span></div>
  </div>

  <div class="room room-wait" role="img" aria-label="緑のソファが並ぶ待合室"><span>待合室</span></div>
  <div class="room room-kids" role="img" aria-label="子どもが遊ぶキッズルーム"><span>キッズルーム</span></div>
  <div class="room room-treat" role="img" aria-label="ベッドが並ぶ施術室"><span>施術室</span></div>
  <div class="room room-wc" role="img" aria-label="清潔なトイレ"><span>トイレ</span></div>
  <div class="abs wide-label">県内最大級の広さ!</div>
  <div class="abs kids-tag">お子様<br>連れ<br>大歓迎!!</div>

  <div class="circle-tag tag-promise">お客様へ<br>お約束</div>
  <h2 class="section-title title-promise">当院は3つの安心をお約束いたします!</h2>

  <div class="promise p1">
    <div class="num">安心1</div>
    <h3>確かな技術</h3>
    <p>国家資格を持つ柔道整復師(筋肉・関節治療の専門家)の治療で安心です。</p>
  </div>
  <div class="promise p2">
    <div class="num">安心2</div>
    <h3>優しい治療</h3>
    <p>体に負担がかからない優しい治療で痛みを取り除きますので安心です。</p>
  </div>
  <div class="promise p3">
    <div class="num">安心3</div>
    <h3>丁寧な症状説明</h3>
    <p>いつ治り、どうして痛いのかをいつも丁寧に説明しますので安心です。</p>
    <div class="small">※個別の解説書も作成しております。</div>
  </div>
  <div class="promise-photo pp1" role="img" aria-label="柔道整復師の免許証"></div>
  <div class="promise-photo pp1b" role="img" aria-label="笑顔の施術スタッフ"></div>
  <div class="promise-photo pp2" role="img" aria-label="うつ伏せの患者に優しく施術する様子"></div>
  <div class="promise-photo pp3" role="img" aria-label="患者に症状を説明するスタッフ"></div>

  <div class="circle-tag tag-care">丁寧な<br>施術</div>
  <h2 class="section-title title-care">こんな痛みを施術します。</h2>
  <div class="abs bubble">お気軽にご相談ください。</div>
  <div class="abs pains">
    <div class="pain-row"><span class="hi w1">交通事故のむちうち</span><span class="w2">寝違い</span><span class="w3">腰の痛み</span><span>ぎっくり腰</span></div>
    <div class="pain-row"><span class="w2" style="width:56px">腰痛</span><span style="width:70px">しびれ</span><span style="width:70px">突き指</span><span style="width:160px">スポーツによるケガ</span><span>肉ばなれ</span></div>
    <div class="pain-row"><span style="width:90px">膝の痛み</span><span style="width:98px">足のねんざ</span><span>骨折・脱臼・だぼく・ねんざなど</span></div>
  </div>

  <div class="abs steps">
    <div class="steps-head">施術の内容<small>お一人お一人に合った治療を致します!</small></div>
    <div class="step-row">
      <div class="step"><i>1</i><b>問診</b><em>症状を詳しく<br>お聞かせ下さい</em><div class="shot" role="img" aria-label="問診の様子"></div></div>
      <div class="step"><i>2</i><b>理学検査</b><em>体の状態を<br>確認します</em><div class="shot" role="img" aria-label="理学検査の様子"></div></div>
      <div class="step"><i>3</i><b>電気治療</b><em>痛みを<br>和らげます</em><div class="shot" role="img" aria-label="電気治療の様子"></div></div>
      <div class="step"><i>4</i><b>マッサージ</b><em>筋肉を<br>ほぐします</em><div class="shot" role="img" aria-label="マッサージの様子"></div></div>
    </div>
  </div>

  <div class="abs insurance">各種保険取扱<small>交通事故／労災指定</small></div>
  <div class="abs price">
    <h4>料金の目安</h4>
    <table>
      <tr><td colspan="2">初診料</td><td>2,000円</td></tr>
      <tr><td rowspan="2" class="ins">保険<br>適用</td><td>1割負担</td><td>200円前後</td></tr>
      <tr><td>3割負担</td><td>500円前後</td></tr>
    </table>
  </div>
  <div class="abs price-note">※保険適用外の施術を行った場合は、別途費用がかかります。</div>

  <footer class="abs footer"></footer>
  <div class="abs foot-brand">
    <div class="name"><span class="dot-mark"></span>ルナヒル整骨院</div>
    <div class="sub">soft line 美容整体院<span>併設</span></div>
  </div>
  <table class="abs schedule">
    <tr><th class="time">受付時間</th><th>月</th><th>火</th><th>水</th><th>木</th><th>金</th><th>土</th><th>日・祝</th></tr>
    <tr><td class="time">午前<br>9:30~13:00</td><td class="dot">●</td><td class="dot">●</td><td class="dot">●</td><td class="dot">●</td><td class="dot">●</td><td class="dot">●</td><td class="dot">●</td></tr>
    <tr><td class="time">午後<br>15:00~20:00</td><td class="dot">●</td><td class="dot">●</td><td class="dot">●</td><td>—</td><td class="dot">●</td><td>—</td><td>—</td></tr>
  </table>
  <div class="abs contact">
    <div class="where">若宮桜台ショッピングセンター内</div>
    <div class="addr">〒340-0217</div>
    <div class="addr">北葉郡若宮町桜台1024-3　ルナヒル整骨院</div>
    <div class="tel">TEL:048-312-7759<span>ご予約優先</span></div>
    <div class="url">http://hana-riku.com/<span class="search">ルナヒル整骨院</span><span class="search-btn">検索</span></div>
  </div>
  <div class="abs map" role="img" aria-label="ショッピングセンター周辺の案内地図"></div>

</div>
</body>
</html>
```